Web page design for technology solution company
Velmork Inc.
Dear PH,
Kindly star rate #83 it will help me to go through.
Thanks!
Hi PH,
Any feedback for #52
Thanks
Kindly check your private messages.
#57 and #58 - don't need the extra info. Stick with your earlier versions - like those better. They're simple and not 'overloaded'
#55, #56 - like the simplicity but don't like the dark background
Hi PH, please check your private message. thanks
#13 and #19 - can we see the design without the graphics?
#20 -#24 - much better with the lighter background!
@PH
Kindly check your private message box on the top right & reply asap with your feedback.Thanks
#10 - #12. They seem interesting but on the darker side. Can we see them with a white background?
#9 - Nice and clean design. It's unique and colors are nicely coordinated. Can you find a place for social media icons?
#1 - #5 . Some of the designs look interesting but the background is too dark. Can we see the same with white background?
PH please check your private message
Perin Koldesh

```html
<!DOCTYPE html>
<html lang="en">
<head>
<meta charset="utf-8">
<title>Velmork Inc. — Technology Solutions</title>
<link href="https://fonts.googleapis.com/css2?family=Oswald:wght@400;500;700&family=PT+Serif&family=Open+Sans:wght@400;600&display=swap" rel="stylesheet">
<style>
  :root {
    --bar-dark: #1c1c1c;
    --bar-mid: #2e2e2e;
    --page-top: #ececec;
    --page-bottom: #f7f7f7;
    --accent: #b5bd35;
    --ink: #333333;
    --ink-soft: #555555;
    --muted: #8a8a8a;
    --nav-muted: #9c9c9c;
    --white: #ffffff;
    --panel: #f4f4f4;
    --button: #3a3a3a;
  }
  * { margin: 0; padding: 0; box-sizing: border-box; }
  html, body { width: 1200px; height: 785px; overflow: hidden; }
  body {
    position: relative;
    background: linear-gradient(to bottom, var(--page-top) 0, var(--page-bottom) 260px, var(--page-bottom) 100%);
    font-family: "PT Serif", Georgia, serif;
    color: var(--ink);
  }

  /* Header */
  .site-header {
    position: absolute; left: 0; top: 0; width: 1200px; height: 43px;
    background: linear-gradient(to bottom, var(--bar-mid), var(--bar-dark));
  }
  .brand {
    position: absolute; left: 282px; top: 6px;
    display: flex; align-items: center; gap: 10px;
  }
  .brand-mark { width: 22px; height: 22px; background: var(--accent); }
  .brand-name {
    font-family: "Oswald", sans-serif; font-weight: 700; font-size: 26px;
    color: var(--accent); line-height: 30px;
  }
  .main-nav {
    position: absolute; right: 250px; top: 13px;
    display: flex; gap: 22px;
    font-family: "Open Sans", Arial, sans-serif; font-size: 14px;
  }
  .main-nav a { color: var(--nav-muted); text-decoration: none; }
  .main-nav a.is-current { color: var(--white); }

  /* Slider */
  .hero {
    position: absolute; left: 283px; top: 48px; width: 665px; height: 132px;
    background: linear-gradient(to bottom, #fbfbfb, #e9e9e9);
    box-shadow: 0 2px 6px rgba(0,0,0,.25);
  }
  .hero-title {
    position: absolute; left: 185px; top: 8px;
    font-family: "Oswald", sans-serif; font-weight: 700; font-size: 28px;
    color: var(--ink); letter-spacing: .5px;
  }
  .hero-text {
    position: absolute; left: 12px; top: 48px; width: 430px;
    font-size: 10px; line-height: 12px; color: var(--ink-soft);
  }
  .hero-visual {
    position: absolute; left: 480px; top: 8px; width: 175px; height: 112px;
    background: radial-gradient(ellipse at 60% 55%, #9fb3c6 0, #d7dde3 55%, #f1f1f1 100%);
    border-radius: 6px;
  }
  .hero-dots {
    position: absolute; left: 260px; top: 113px; display: flex; gap: 5px;
  }
  .hero-dots span { width: 11px; height: 11px; border-radius: 50%; background: #9a9a9a; }
  .hero-dots span.is-active { background: #5a5a5a; }
  .button {
    display: inline-block; background: var(--button); color: var(--white);
    font-family: "Oswald", sans-serif; font-size: 10px; letter-spacing: .5px;
    border-radius: 9px; text-align: center; text-decoration: none;
  }
  .hero .button { position: absolute; left: 364px; top: 112px; width: 66px; height: 14px; line-height: 14px; font-size: 9px; }
  .hero-arrow { position: absolute; top: 102px; width: 28px; height: 28px; }
  .hero-arrow.prev { left: 250px; }
  .hero-arrow.next { left: 942px; }

  .intro-text {
    position: absolute; left: 283px; top: 218px; width: 420px;
    font-size: 9px; line-height: 11px; color: var(--ink-soft);
  }

  .section-title {
    font-family: "Oswald", sans-serif; font-weight: 500; color: var(--accent);
    text-transform: uppercase;
  }

  /* Services */
  .services { position: absolute; left: 286px; top: 280px; width: 400px; }
  .services .section-title { font-size: 22px; letter-spacing: -.3px; }
  .service-grid {
    list-style: none; margin-top: 24px;
    display: grid; grid-template-columns: 145px 145px; row-gap: 36px;
  }
  .service-grid li {
    font-family: "Oswald", sans-serif; font-size: 11px; color: var(--ink);
    padding-left: 14px; position: relative; height: 22px;
  }
  .service-grid li::before {
    content: ""; position: absolute; left: 0; top: 4px;
    border-left: 6px solid var(--ink); border-top: 4px solid transparent; border-bottom: 4px solid transparent;
  }

  /* Recent updates */
  .updates { position: absolute; left: 800px; top: 262px; width: 160px; }
  .updates .section-title { font-size: 20px; text-align: center; }
  .updates-list { list-style: none; margin-top: 12px; }
  .updates-list li {
    font-family: "Open Sans", Arial, sans-serif; font-size: 9px; font-weight: 600;
    color: var(--muted); height: 30px; line-height: 14px;
  }

  /* Hire us */
  .hire { position: absolute; left: 283px; top: 532px; width: 500px; }
  .hire .section-title { font-size: 26px; }
  .hire-text {
    margin-top: 2px; width: 410px;
    font-size: 10px; line-height: 12px; color: var(--ink-soft);
  }
  .hire .button { position: absolute; left: 400px; top: 150px; width: 98px; height: 22px; line-height: 22px; font-size: 12px; border-radius: 11px; }

  /* Footer */
  .site-footer {
    position: absolute; left: 0; bottom: 0; width: 1200px; height: 34px;
    background: var(--bar-dark); color: var(--white);
    font-family: "Oswald", sans-serif; font-size: 19px; text-align: center; line-height: 34px;
  }
</style>
</head>
<body>
  <header class="site-header">
    <div class="brand">
      <span class="brand-mark"></span>
      <span class="brand-name">Velmork Inc.</span>
    </div>
    <nav class="main-nav">
      <a href="#" class="is-current">Home</a>
      <a href="#">About</a>
      <a href="#">Products &amp; Services</a>
      <a href="#">Contact Us</a>
    </nav>
  </header>

  <section class="hero">
    <h1 class="hero-title">WELCOME</h1>
    <p class="hero-text">We build dependable technology solutions for growing teams. Our engineers plan, design and support systems that keep your business running smoothly every day. Talk to us about software, networks and cloud services tailored to your goals.</p>
    <div class="hero-visual" role="img" aria-label="Smartphone surrounded by floating app icons"></div>
    <div class="hero-dots"><span class="is-active"></span><span></span><span></span><span></span></div>
    <a href="#" class="button">READ MORE</a>
  </section>
  <svg class="hero-arrow prev" viewBox="0 0 28 28" aria-hidden="true"><circle cx="14" cy="14" r="13" fill="#3a3a3a"/><path d="M17 8 L9 14 L17 20 Z" fill="#fff"/></svg>
  <svg class="hero-arrow next" viewBox="0 0 28 28" aria-hidden="true"><circle cx="14" cy="14" r="13" fill="#3a3a3a"/><path d="M11 8 L19 14 L11 20 Z" fill="#fff"/></svg>

  <p class="intro-text">From first consultation to final rollout, we stay with you. Our team handles setup, training and ongoing maintenance so your staff can focus on the work that matters most to your customers.</p>

  <section class="services">
    <h2 class="section-title">Summary of Services</h2>
    <ul class="service-grid">
      <li>PODCAST</li><li>PODCAST</li>
      <li>LIVE SHOW</li><li>LIVE SHOW</li>
      <li>SPONSORSHIP</li><li>SPONSORSHIP</li>
    </ul>
  </section>

  <aside class="updates">
    <h2 class="section-title">Recent Updates</h2>
    <ul class="updates-list">
      <li>COMPANY QUARTERLY PROFIT</li>
      <li>COMPANY QUARTERLY PROFIT</li>
      <li>COMPANY QUARTERLY PROFIT</li>
      <li>COMPANY QUARTERLY PROFIT</li>
      <li>COMPANY QUARTERLY PROFIT</li>
      <li>COMPANY QUARTERLY PROFIT</li>
      <li>COMPANY QUARTERLY PROFIT</li>
      <li>COMPANY QUARTERLY PROFIT</li>
    </ul>
  </aside>

  <section class="hire">
    <h2 class="section-title">Hire Us</h2>
    <p class="hire-text">Need a partner for your next project? Velmork Inc. brings years of experience in custom software, infrastructure planning and technical support. We listen first, then propose clear solutions with honest timelines and fair pricing. Whether you run a small office or a large enterprise, our specialists adapt to your needs. We deliver secure systems, responsive service and lasting results. Contact our team today and let us help your business grow with technology that simply works.</p>
    <a href="#" class="button">READ MORE</a>
  </section>

  <footer class="site-footer">COPYRIGHTS 2012</footer>
</body>
</html>
```